Harbor Allied BC

I have a baseline business card that I would like to spruce up!

I actually like this business card. I just want to find a way to have all the information below on it and it too look balanced and professional.

Target Market(s)

Small to medium sized companies - Health Insurance Consulting

Industry/Entity Type

Health Insurance

Contact Information for Business Card

The information I would like included on the business card is:

- Harbor Allied Southridge Title and logo
- Tessa Wrenfield
- Business title: Principal
- 4192 Cobalt Ridge Rd Suite D-117 Alder Cove, WA 98999
- Employee Benefits Consulting & (Wellness Consulting) optional
- tessa@harboralliedsr.example
- cell: 425-555-0183

Font styles to use
Other font styles liked:
• I like the font it is currently in but am open to others.

Requirements
Must have
• I like the logo and the color scheme. I even like the layout. I just need to fine tune it!

```html
<!DOCTYPE html>
<html lang="en">
<head>
<meta charset="utf-8">
<title>Harbor Allied Southridge – Business Card</title>
<link href="https://fonts.googleapis.com/css2?family=Lato:wght@300;400;700&display=swap" rel="stylesheet">
<style>
  :root {
    --brand-green: #0a8a4a;
    --ink: #1a1a1a;
    --muted: #555555;
    --rule: #9a9a9a;
    --paper: #ffffff;
    --stripe: #111111;
    --backdrop: #e6e7e8;
  }
  * { box-sizing: border-box; margin: 0; padding: 0; }
  html, body {
    width: 1200px; height: 900px; overflow: hidden;
    background: var(--backdrop);
    font-family: "Lato", Arial, sans-serif;
    color: var(--ink);
  }
  .canvas { position: relative; width: 1200px; height: 900px; }
  .card {
    position: absolute; left: 260px;
    width: 680px; height: 390px;
    background: var(--paper);
    overflow: hidden;
    box-shadow: 0 2px 8px rgba(0,0,0,.12);
  }
  .card--brand { top: 45px; }
  .card--contact { top: 465px; }

  /* Lockup */
  .lockup { position: absolute; display: flex; align-items: center; }
  .lockup__mark {
    width: 70px; height: 70px; border-radius: 50%;
    background: var(--brand-green); flex: none;
  }
  .lockup__name {
    margin-left: 16px;
    font-weight: 400; font-size: 27px; letter-spacing: .5px;
    line-height: 1.05; color: var(--ink); text-transform: uppercase;
  }
  .lockup__name span { display: block; text-align: right; font-size: 17px; letter-spacing: 1px; }
  .lockup__divider {
    width: 1px; height: 74px; background: var(--rule);
    margin: 0 16px 0 20px; align-self: flex-end;
  }
  .lockup__descriptor {
    font-weight: 300; font-size: 15px; line-height: 1.15; color: var(--muted);
    align-self: flex-end;
  }
  .card--brand .lockup { left: 110px; top: 120px; }
  .services {
    position: absolute; left: 0; right: 0; top: 262px;
    text-align: center; font-size: 18px; color: var(--ink);
  }
  .services__dot {
    display: inline-block; width: 7px; height: 7px; border-radius: 50%;
    background: var(--brand-green); margin: 0 8px; vertical-align: middle;
  }

  /* Contact side */
  .card--contact .lockup { left: 40px; top: 40px; }
  .contact {
    position: absolute; left: 40px; top: 160px;
    font-size: 18px; line-height: 1.3;
  }
  .contact__phone { display: flex; align-items: center; gap: 10px; margin-bottom: 10px; }
  .contact__phone svg { width: 12px; height: 16px; }
  .person { position: absolute; right: 70px; top: 192px; }
  .person__name { font-size: 30px; color: var(--brand-green); font-weight: 400; }
  .person__title { font-size: 18px; font-weight: 700; margin-top: 2px; }
  .band { position: absolute; left: 0; top: 0; width: 680px; height: 390px; }
  .email {
    position: absolute; left: 250px; bottom: 20px;
    font-size: 19px; color: var(--paper);
  }
</style>
</head>
<body>
<main class="canvas">

  <section class="card card--brand" aria-label="Business card front">
    <div class="lockup">
      <div class="lockup__mark" aria-hidden="true"></div>
      <div class="lockup__name">Harbor Allied<span>Southridge</span></div>
      <div class="lockup__divider"></div>
      <div class="lockup__descriptor">Employee<br>Benefits<br>Services</div>
    </div>
    <p class="services">Employee Benefits Consulting<span class="services__dot"></span>Wellness Consulting</p>
  </section>

  <section class="card card--contact" aria-label="Business card back">
    <svg class="band" viewBox="0 0 680 390" aria-hidden="true">
      <path d="M0 286 C200 296 450 314 680 324 L680 390 L0 390 Z" fill="var(--stripe)"/>
      <path d="M0 296 C200 306 450 326 680 338 L680 390 L0 390 Z" fill="var(--paper)"/>
      <path d="M0 300 C200 311 450 332 680 345 L680 390 L0 390 Z" fill="var(--brand-green)"/>
    </svg>

    <div class="lockup">
      <div class="lockup__mark" aria-hidden="true"></div>
      <div class="lockup__name">Harbor Allied<span>Southridge</span></div>
      <div class="lockup__divider"></div>
      <div class="lockup__descriptor">Employee<br>Benefits<br>Services</div>
    </div>

    <div class="contact">
      <p class="contact__phone">
        <svg viewBox="0 0 12 16" aria-hidden="true"><rect x="1" y="1" width="10" height="14" rx="2" fill="#0a8a4a"/><rect x="3" y="3" width="6" height="8" fill="#fff"/></svg>
        425-555-0183
      </p>
      <p>4192 Cobalt Ridge Rd Suite D-117<br>Alder Cove, WA 98999</p>
    </div>

    <div class="person">
      <p class="person__name">Tessa Wrenfield</p>
      <p class="person__title">Principal</p>
    </div>

    <p class="email">tessa@harboralliedsr.example</p>
  </section>

</main>
</body>
</html>
```